Classy business card for accounting firm

We're looking for a new business card for our accounting firm. Our logo was designed by Brandolith, so all of the design info we would like to use has been provided. The specific font provided isn't required to be used.

We want the card to look classy and elegent. Probably more minimalistic, but still with some pops of color.

The options we would like to include on the card are as follows:
1. Main office phone line
2. Direct phone line
3. Email address
4. Website URL
5. Name
6. Title (CEO, President, etc.)
7. Firm Address

The design and card should be double sided!!! The drop down box in the project brief for some reason is defaulting to single sided. Not sure why this is happening.

Thanks!

Contact Information for Business Card

The options we would like to include on the card are as follows: 1. Main office phone line 2. Direct phone line 3. Email address 4. Website URL 5. Name 6. Title (CEO, President, etc.) 7. Firm Address

Requirements
Must have
• Card must be double sided.

```html
<!DOCTYPE html>
<html lang="en">
<head>
<meta charset="utf-8">
<title>Tallyford Associates — Business Card</title>
<link href="https://fonts.googleapis.com/css2?family=Lato:wght@400;700&display=swap" rel="stylesheet">
<style>
  :root {
    --page: #ecebe8;
    --card: #ffffff;
    --ink: #6b6c6f;
    --ink-dark: #3a3a3c;
    --orange: #f7892b;
    --green: #b3c14a;
  }
  * { box-sizing: border-box; margin: 0; padding: 0; }
  html, body { width: 1200px; height: 960px; overflow: hidden; }
  body {
    background: var(--page);
    display: flex;
    flex-direction: column;
    align-items: center;
    justify-content: center;
    gap: 56px;
    font-family: "Lato", sans-serif;
  }
  .card {
    position: relative;
    width: 700px;
    height: 400px;
    background: var(--card);
    box-shadow: 0 6px 20px rgba(0,0,0,0.12);
  }

  /* Brand name: plain text with one square */
  .brand {
    display: flex;
    align-items: center;
    gap: 12px;
  }
  .brand__square {
    width: 18px;
    height: 18px;
    background: var(--orange);
    flex: none;
  }
  .brand__name {
    font-family: "Lato", sans-serif;
    font-weight: 700;
    color: var(--ink);
  }
  .descriptor {
    font-family: "Lato", sans-serif;
    font-weight: 400;
    color: var(--ink-dark);
  }

  /* Front side */
  .card--brand {
    display: flex;
    flex-direction: column;
    align-items: center;
    justify-content: center;
  }
  .card--brand .brand__name { font-size: 34px; }
  .card--brand .brand__square { width: 22px; height: 22px; }
  .card--brand .descriptor { margin-top: 8px; font-size: 15px; }

  /* Contact side */
  .card--contact .brand { position: absolute; left: 34px; top: 32px; }
  .card--contact .brand__name { font-size: 23px; }
  .card--contact .descriptor {
    position: absolute; left: 64px; top: 66px;
    font-size: 13px;
  }

  .divider {
    position: absolute;
    left: 34px;
    top: 246px;
    width: 500px;
    height: 1.5px;
    background: var(--green);
  }
  .person {
    position: absolute;
    right: 34px;
    top: 214px;
    text-align: right;
  }
  .person__name {
    font-weight: 700;
    font-size: 21px;
    letter-spacing: 0.06em;
    color: var(--orange);
    text-transform: uppercase;
  }
  .person__title {
    font-size: 16px;
    color: var(--ink-dark);
    margin-top: 4px;
  }
  .contacts {
    position: absolute;
    left: 34px;
    top: 270px;
    list-style: none;
    font-size: 15px;
    color: var(--ink-dark);
    line-height: 1.45;
  }
  .contacts li { display: flex; align-items: center; gap: 10px; }
  .contacts svg { width: 12px; height: 12px; flex: none; }
  .address {
    position: absolute;
    right: 34px;
    bottom: 30px;
    text-align: right;
    font-style: normal;
    font-size: 15px;
    line-height: 1.4;
    color: var(--ink-dark);
  }
</style>
</head>
<body>

  <section class="card card--brand" aria-label="Card front">
    <div class="brand">
      <span class="brand__square"></span>
      <span class="brand__name">Tallyford Associates</span>
    </div>
    <p class="descriptor">Accounting and tax advisory</p>
  </section>

  <section class="card card--contact" aria-label="Card back">
    <div class="brand">
      <span class="brand__square"></span>
      <span class="brand__name">Tallyford Associates</span>
    </div>
    <p class="descriptor">Accounting and tax advisory</p>

    <div class="divider"></div>

    <div class="person">
      <div class="person__name">Daniel Reyes</div>
      <div class="person__title">President</div>
    </div>

    <ul class="contacts">
      <li>
        <svg viewBox="0 0 12 12" aria-hidden="true"><path d="M2.5 1 L4.5 1 L5 3.5 L3.8 4.4 Q4.8 6.6 7.2 8 L8.2 6.9 L11 7.5 L11 9.5 Q10.5 11 8.8 11 Q1 10 1 2.8 Q1 1 2.5 1 Z" fill="var(--orange)"/></svg>
        000 0000 000
      </li>
      <li>
        <svg viewBox="0 0 12 12" aria-hidden="true"><rect x="3" y="0.8" width="6" height="10.4" rx="1" fill="none" stroke="var(--orange)" stroke-width="1.3"/><circle cx="6" cy="9.3" r="0.7" fill="var(--orange)"/></svg>
        000 0000 000
      </li>
      <li>
        <svg viewBox="0 0 12 12" aria-hidden="true"><rect x="0.5" y="2.5" width="11" height="7.5" fill="var(--orange)"/><path d="M0.5 2.5 L6 7 L11.5 2.5" fill="none" stroke="#fff" stroke-width="1"/></svg>
        hello@tallyford.example
      </li>
      <li>
        <svg viewBox="0 0 12 12" aria-hidden="true"><circle cx="6" cy="6" r="5" fill="none" stroke="var(--orange)" stroke-width="1.1"/><ellipse cx="6" cy="6" rx="2.2" ry="5" fill="none" stroke="var(--orange)" stroke-width="0.9"/><line x1="1" y1="6" x2="11" y2="6" stroke="var(--orange)" stroke-width="0.9"/></svg>
        www.tallyford.example
      </li>
    </ul>

    <address class="address">
      218 Harrow Lane<br>
      Suite 400, Fairview, DC 20099
    </address>
  </section>

</body>
</html>
```